VELMAR, an e-commerce website with a twist, providing consumer-to-consumer and business-to-consumer sa

I have only uploaded 10 wire-frame pages of the website. These pages have been chosen for the different lay-outs and should give an idea of what will be needed. There are many more that I won’t upload yet, I aim to choose a winner first then there will be a high possibility that the winner will get the chance to do the design work for these later.
The design I have in mind is to keep it clean and easy with no/minimal fancy fonts and hieroglyphics. The logo is white with an orange highlight on a solid background of black, please note that the logo is white on a black background and is not a black box with white lettering, trust that makes sense. I like the idea of the top part of the website being black all the way across. I don’t see the need for more than 3 colours in the actual base website (the pictures and adverts added by users will add other colours). Although orange is the highlight colour in the logo I am open to suggestions on this, so long as the highlight colour features throughout the site.

Website width is 1220px, all pages in the PDF are 1220px

Logo font is Rezlong

The company is going to be like tradu, but much more focused on raising money for charity and humanitarian relief.

Target Market(s)

the modern era of smartphones and the sharing community

Industry/Entity Type

Business

Number of Pages Required

5+ page

Font styles to use
Sans Serif
Other font styles liked:
• rezlong

Colors
faa54b
f78f20
ffffff
000000
fbfbfb
f5f5f5

Requirements
Nice to have
• Although orange is the highlight colour in the logo I am open to suggestions on this, so long as the highlight colour features throughout the site.

```html
<!DOCTYPE html>
<html lang="en">
<head>
<meta charset="utf-8">
<title>VELMAR – Home</title>
<link href="https://fonts.googleapis.com/css2?family=Comfortaa:wght@700&family=Open+Sans:wght@400;600;700;800&display=swap" rel="stylesheet">
<style>
:root{
  --orange:#f78f20;
  --orange-light:#faa54b;
  --black:#000;
  --white:#fff;
  --off:#fbfbfb;
  --grey-bg:#f5f5f5;
  --grey-line:#d4d4d4;
  --grey-text:#8a8a8a;
  --dark-text:#222;
  --footer-text:#d8d8d8;
}
*{box-sizing:border-box;margin:0;padding:0}
html,body{width:728px;height:1200px;overflow:hidden;background:var(--white)}
body{position:relative;font-family:"Open Sans",Arial,sans-serif;color:var(--dark-text)}
.abs{position:absolute}
.display{font-family:"Comfortaa","Open Sans",sans-serif;font-weight:700;letter-spacing:.5px}

/* top strip */
.util-bar{left:0;top:0;width:728px;height:24px;background:var(--orange);font-size:8.5px;color:var(--white)}
.util-bar a{color:var(--white);text-decoration:none}
.util-left{left:20px;top:0;height:24px;display:flex;align-items:center}
.util-left a{padding:0 8px;border-right:1px solid rgba(255,255,255,.5);line-height:24px}
.util-left a:first-child{padding-left:8px}
.util-right{left:340px;top:0;height:24px;display:flex;align-items:center}
.util-right a{padding:0 8px;border-left:1px solid rgba(255,255,255,.5);line-height:24px}
.util-right a:first-child{border-left:none}
.util-search{left:551px;top:0;width:148px;height:24px;background:var(--orange-light);display:flex;align-items:center;padding-left:10px;gap:4px}

/* header */
.masthead{left:0;top:24px;width:728px;height:72px;background:var(--black)}
.brand{left:29px;top:20px;font-size:30px;font-weight:700;color:var(--white);display:flex;align-items:center;gap:6px}
.brand-dot{width:8px;height:8px;background:var(--orange);display:inline-block}
.main-nav{right:28px;top:18px;display:flex;gap:22px;color:#ccc;font-size:9.5px}
.main-nav .nav-item{display:flex;flex-direction:column;align-items:center;gap:6px}
.main-nav svg{width:18px;height:18px;fill:#bbb}

/* hero */
.video-tile{left:22px;width:194px;background:linear-gradient(135deg,#8f8a80,#5a5c58);display:flex;flex-direction:column;align-items:center;justify-content:center;gap:6px;color:var(--white);font-size:12px}
.play{width:42px;height:42px;border:2px solid var(--white);border-radius:50%;display:flex;align-items:center;justify-content:center}

.search-panel{left:226px;top:111px;width:282px;height:278px;border:1px solid var(--grey-line);background:var(--white);padding:0 0 0 20px}
.panel-title{font-size:17px;color:var(--black);margin-top:14px}
.field-label{color:var(--orange);font-size:11.5px}
.field{background:var(--grey-bg);border:1px solid var(--grey-line);height:24px;font-size:10px;color:var(--grey-text);display:flex;align-items:center;padding-left:8px}
.help{width:12px;height:12px;border-radius:50%;background:#bbb;color:var(--white);font-size:9px;font-weight:700;display:flex;align-items:center;justify-content:center}
.btn-search{left:20px;top:221px;width:248px;height:30px;background:linear-gradient(var(--orange-light),var(--orange));color:var(--white);font-size:15px;display:flex;align-items:center;justify-content:center;border-radius:2px}

.featured{left:514px;top:111px;width:194px;height:278px;border:1px solid var(--grey-line);background:var(--white)}
.featured-head{height:34px;background:var(--grey-bg);color:var(--orange);font-size:15px;padding:8px 0 0 16px}
.product{left:15px;width:170px;display:flex;gap:8px}
.product-img{width:78px;height:62px;border:1px solid var(--grey-line);flex:none;background:linear-gradient(135deg,#e9e9e9,#9a9a9a)}
.product-title{font-size:9.5px;color:var(--dark-text);font-weight:600;margin-top:-2px}
.product-desc{font-size:7.4px;color:var(--grey-text);line-height:12px;margin-top:3px}
.product-link{font-size:7.5px;color:var(--orange);margin-top:2px}

/* course ad */
.course-ad{left:30px;top:404px;width:671px;height:69px;background:linear-gradient(90deg,#2f7fd6,#2aa0a7 55%,#24a460)}
.ad-logo-box{left:87px;top:9px;width:128px;height:50px;background:var(--white);display:flex;align-items:center;justify-content:center;gap:6px;font-size:13px;color:#555}
.ad-logo-box span.sq{width:12px;height:12px;background:#3b82e0}
.ad-list{font-size:8.7px;font-weight:700;color:var(--white);line-height:14px}
.ad-list li{list-style:none}
.ad-list li::before{content:"";display:inline-block;border-left:6px solid #f3c623;border-top:3.5px solid transparent;border-bottom:3.5px solid transparent;margin-right:5px}

/* feedback */
.feedback{left:0;top:498px;width:728px;height:232px;background:var(--orange)}
.notch{left:350px;top:498px;width:0;height:0;border-left:14px solid transparent;border-right:14px solid transparent;border-top:14px solid var(--white)}
.section-title{font-size:20px}
.feedback-title{left:0;top:526px;width:728px;text-align:center;color:var(--white)}
.quote-card{top:562px;width:211px;height:121px;border:1px solid rgba(255,255,255,.85);color:var(--white);padding:10px 14px 0 26px;font-size:8.8px;line-height:16px}
.quote-card .mark{position:absolute;font-size:18px;font-family:Georgia,serif;font-style:italic;line-height:1}
.author{left:26px;top:83px;display:flex;align-items:center;gap:5px}
.avatar{width:26px;height:26px;border-radius:50%;background:#e7d6c4;border:2px solid var(--white)}
.author b{font-size:9px;font-weight:600;display:block;line-height:12px}
.author small{font-size:7.5px;display:block;line-height:11px}
.pill{left:240px;top:712px;width:245px;height:31px;border-radius:16px;background:var(--orange-light);color:var(--white);font-size:11px;display:flex;align-items:center;justify-content:center}

/* deals ad */
.deals-ad{left:34px;top:769px;width:666px;height:77px;background:linear-gradient(90deg,#f6b200,#ffc400);border:1px solid #c99200}
.deals-art{left:0;top:0;width:105px;height:75px;background:linear-gradient(135deg,#e7a26a,#d65f8a)}
.deals-small{left:100px;top:10px;font-size:13px;font-weight:800;color:#1e1e1e;line-height:14px}
.deals-big{left:337px;top:14px;font-size:21px;font-weight:800;color:#1e1e1e;line-height:26px;font-family:Georgia,serif}
.learn{left:542px;top:18px;width:106px;height:25px;background:linear-gradient(#3f8cf0,#1a5fd0);border:2px solid #cfe0ff;border-radius:3px;color:var(--white);font-size:12px;font-weight:700;display:flex;align-items:center;justify-content:center}
.adchoice{left:651px;top:1px;width:12px;height:10px;border:1px solid #3b8ff0;background:var(--white)}

/* charities */
.charities-title{left:34px;top:878px;color:#4a4a4a}
.charity{width:110px;text-align:center;color:#8d8d8d;font-weight:700;font-size:11px;display:flex;flex-direction:column;align-items:center;gap:6px}
.charity .shape{width:26px;height:26px;background:#b8b8b8}
.charity .shape.round{border-radius:50%}

.promo-yellow{left:374px;top:872px;width:324px;height:95px;background:radial-gradient(circle at 50% 40%,#ffd21c,#f3a70c);text-align:center}
.promo-yellow h3{font-weight:800;color:var(--white);font-size:14px;line-height:14px;margin-top:24px;text-shadow:0 1px 0 #c77b00}
.promo-yellow p{font-size:6.5px;color:#3461b4;margin-top:10px;font-weight:600}
.promo-yellow p.sizes{color:#c0392b;margin-top:1px;font-size:5.5px}
.promo-teal{left:374px;top:978px;width:324px;height:96px;background:linear-gradient(90deg,#3a9fbb,#44b3c8)}
.promo-person{left:8px;top:8px;width:80px;height:88px;background:linear-gradient(#4a6e7c,#1e2e34)}
.promo-teal h3{position:absolute;left:112px;top:16px;color:var(--white);font-weight:800;font-size:15px;line-height:18px}
.chip{position:absolute;top:62px;height:20px;border:1px solid var(--white);color:var(--white);font-size:8px;font-weight:700;display:flex;align-items:center;justify-content:center;gap:4px}
.chip.dark{border-color:#173845;color:#173845}

/* footer */
.site-footer{left:0;top:1107px;width:728px;height:93px;background:var(--black);color:var(--footer-text)}
.footer-links{left:42px;top:22px;font-size:11px;display:flex;gap:6px}
.copyright{left:42px;top:51px;font-size:9.5px}
.social{right:34px;top:23px;display:flex;gap:4px}
.social span{width:15px;height:15px;background:#e2e2e2;border-radius:2px}
.legal{right:34px;top:54px;font-size:9.5px;color:#bbb}
</style>
</head>
<body>

<header>
  <div class="abs util-bar">
    <nav class="abs util-left"><a>Notification</a><a>News</a><a style="border-right:none">List Item</a></nav>
    <nav class="abs util-right"><a>Contact Us</a><a>Help</a><a>Terms and Conditions</a></nav>
    <div class="abs util-search">
      <svg width="9" height="9" viewBox="0 0 10 10"><circle cx="4" cy="4" r="3" fill="none" stroke="#fff" stroke-width="1.4"/><line x1="6.2" y1="6.2" x2="9" y2="9" stroke="#fff" stroke-width="1.4"/></svg>Search
    </div>
  </div>
  <div class="abs masthead">
    <div class="abs brand"><span>VELMAR</span><span class="brand-dot"></span></div>
    <nav class="abs main-nav">
      <div class="nav-item"><svg viewBox="0 0 20 20"><path d="M2 7h16l-2 10H4z"/><path d="M6 7l4-5 4 5" fill="none" stroke="#bbb" stroke-width="1.6"/></svg>Shopping Basket</div>
      <div class="nav-item"><svg viewBox="0 0 20 20"><path d="M10 18L2 9.5C0 7 1.5 2.5 5.5 2.5c2 0 3.5 1.5 4.5 3 1-1.5 2.5-3 4.5-3 4 0 5.5 4.5 3.5 7z"/></svg>Wish list</div>
      <div class="nav-item"><svg viewBox="0 0 20 20"><rect x="4" y="9" width="12" height="9" rx="1"/><path d="M6.5 9V6a3.5 3.5 0 017 0v3" fill="none" stroke="#bbb" stroke-width="2"/></svg>Sign In</div>
      <div class="nav-item"><svg viewBox="0 0 20 20"><circle cx="10" cy="6" r="4"/><path d="M2 19c0-5 3.5-8 8-8s8 3 8 8z"/></svg>My Account</div>
      <div class="nav-item"><svg viewBox="0 0 20 20"><circle cx="8" cy="8" r="5.5" fill="none" stroke="#bbb" stroke-width="2.2"/><line x1="12" y1="12" x2="18" y2="18" stroke="#bbb" stroke-width="2.6"/></svg>My Recent Searches</div>
    </nav>
  </div>
</header>

<main>
  <section>
    <div class="abs video-tile" style="top:111px;height:133px" role="img" aria-label="Video still: smiling man using a laptop">
      <div class="play"><svg width="14" height="16" viewBox="0 0 14 16"><path d="M2 1l11 7-11 7z" fill="none" stroke="#fff" stroke-width="1.6"/></svg></div>
      <span>What it's about</span>
    </div>
    <div class="abs video-tile" style="top:255px;height:134px;background:linear-gradient(135deg,#9a9a8a,#4f5c4a)" role="img" aria-label="Video still: many hands joined together">
      <div class="play"><svg width="14" height="16" viewBox="0 0 14 16"><path d="M2 1l11 7-11 7z" fill="none" stroke="#fff" stroke-width="1.6"/></svg></div>
      <span>What VELMAR does for charity</span>
    </div>

    <form class="abs search-panel">
      <h2 class="display panel-title">search your product</h2>
      <div class="abs field-label" style="left:20px;top:42px">Product</div>
      <div class="abs field" style="left:20px;top:62px;width:232px">Items</div>
      <div class="abs help" style="left:258px;top:68px">?</div>
      <div class="abs field-label" style="left:20px;top:95px">Location</div>
      <div class="abs field" style="left:20px;top:114px;width:232px">location</div>
      <div class="abs help" style="left:258px;top:120px">?</div>
      <div class="abs field-label" style="left:20px;top:155px">From</div>
      <div class="abs field" style="left:58px;top:150px;width:194px">£</div>
      <div class="abs help" style="left:258px;top:156px">?</div>
      <div class="abs field-label" style="left:20px;top:188px">To</div>
      <div class="abs field" style="left:58px;top:182px;width:194px">£</div>
      <div class="abs help" style="left:258px;top:188px">?</div>
      <div class="abs btn-search display">search</div>
    </form>

    <aside class="abs featured">
      <h2 class="display featured-head">featured product</h2>
      <div class="abs product" style="top:46px">
        <div class="product-img" role="img" aria-label="Product photo: compact camera"></div>
        <div><div class="product-title">Item Tittle here</div><div class="product-desc">Praesent elementum elit at tellus nec ultri cies sit amet</div><div class="product-link">CLICK HERE</div></div>
      </div>
      <div class="abs product" style="top:123px">
        <div class="product-img" role="img" aria-label="Product photo: drawing tablet with pen"></div>
        <div><div class="product-title">Item Tittle here</div><div class="product-desc">Praesent elementum elit at tellus nec ultri cies sit amet</div><div class="product-link">CLICK HERE</div></div>
      </div>
      <div class="abs product" style="top:200px">
        <div class="product-img" role="img" aria-label="Product photo: virtual reality headset"></div>
        <div><div class="product-title">Item Tittle here</div><div class="product-desc">Praesent elementum elit at tellus nec ultri cies sit amet</div><div class="product-link">CLICK HERE</div></div>
      </div>
    </aside>
  </section>

  <aside class="abs course-ad">
    <div class="abs ad-logo-box"><span class="sq"></span>Adsmark</div>
    <ul class="abs ad-list" style="left:244px;top:15px"><li>Quality Instructors</li><li>Live Training</li><li>Small Classes</li></ul>
    <ul class="abs ad-list" style="left:391px;top:15px"><li>Hands-on Learning</li><li>Excellent Student Reviews</li><li>Free Retakes</li></ul>
  </aside>

  <section>
    <div class="abs feedback"></div>
    <div class="abs notch"></div>
    <h2 class="abs display section-title feedback-title">user feedback</h2>

    <article class="abs quote-card" style="left:41px">
      <span class="mark" style="left:22px;top:10px">"</span>
      Praesent elementum elit at tellus nec ultricies sit amet porttitor mattis enim In massa libero interdum nec interdum vel blandit sed nulla In ullamcorper<span class="mark" style="left:156px;top:68px">"</span>
      <div class="abs author"><span class="avatar" role="img" aria-label="Author portrait"></span><div><b>By Author Name</b><small>Location City</small></div></div>
    </article>
    <article class="abs quote-card" style="left:262px">
      <span class="mark" style="left:22px;top:10px">"</span>
      Praesent elementum elit at tellus nec ultricies sit amet porttitor mattis enim In massa libero interdum nec interdum vel blandit sed nulla In<span class="mark" style="left:112px;top:68px">"</span>
      <div class="abs author"><span class="avatar" role="img" aria-label="Author portrait"></span><div><b>By Author Name</b><small>Location City</small></div></div>
    </article>
    <article class="abs quote-card" style="left:482px">
      <span class="mark" style="left:22px;top:10px">"</span>
      Praesent elementum elit at tellus nec ultricies sit amet porttitor mattis enim In massa libero interdum nec interdum vel blandit sed nulla In ullamcorper<span class="mark" style="left:156px;top:68px">"</span>
      <div class="abs author"><span class="avatar" role="img" aria-label="Author portrait"></span><div><b>By Author Name</b><small>Location City</small></div></div>
    </article>

    <div class="abs pill">Leave feedback for a chance to win a price</div>
  </section>

  <aside class="abs deals-ad">
    <div class="abs deals-art" role="img" aria-label="Illustration: shopper holding colourful bags"></div>
    <div class="abs deals-small">Find Exclusive Deals<br>Here!</div>
    <div class="abs deals-big">Up to 70%<br>off!</div>
    <div class="abs learn">Learn More</div>
    <div class="abs adchoice"></div>
  </aside>

  <section>
    <h2 class="abs display section-title charities-title">charities support</h2>
    <div class="abs charity" style="left:24px;top:926px"><span class="shape"></span>Youth Circle</div>
    <div class="abs charity" style="left:136px;top:926px"><span class="shape round"></span>KindHeart</div>
    <div class="abs charity" style="left:249px;top:939px;font-size:22px;font-weight:400">Harbour</div>
    <div class="abs charity" style="left:24px;top:1014px"><span class="shape"></span>Uplift Foundation</div>
    <div class="abs charity" style="left:136px;top:1014px"><span class="shape round"></span>Paw Aid</div>
    <div class="abs charity" style="left:249px;top:1014px"><span class="shape"></span>Relief Corps</div>

    <aside class="abs promo-yellow">
      <h3>BRING IDEAS TO LIFE<br>ACROSS SCREENS</h3>
      <p>THREE STANDARD SIZES</p>
      <p class="sizes">728X90 • 300X250 • 160X600</p>
    </aside>
    <aside class="abs promo-teal">
      <div class="abs promo-person" role="img" aria-label="Photo: businesswoman in glasses"></div>
      <h3>BUSINESS AD EXPANDABLE<br>WITH STREAMLY</h3>
      <div class="chip" style="left:114px;width:52px"><svg width="10" height="10" viewBox="0 0 10 10"><circle cx="5" cy="5" r="5" fill="#fff"/><path d="M4 3l3 2-3 2z" fill="#3a9fbb"/></svg>VIDEO</div>
      <div class="chip dark" style="left:174px;width:98px">PSD INCLUDED</div>
    </aside>
  </section>
</main>

<footer class="abs site-footer">
  <nav class="abs footer-links"><span>About VELMAR</span>|<span>Safety Hub</span>|<span>Resolution Hub</span>|<span>Vendor Hub</span>|<span>Partner Hub</span>|<span>Chairty Hub</span></nav>
  <div class="abs copyright">© 2017 Company Name&nbsp; All right reserved</div>
  <div class="abs social" aria-label="Social links"><span></span><span></span><span></span><span></span><span></span><span></span></div>
  <div class="abs legal">Advertise &nbsp;|&nbsp; Sitemap</div>
</footer>

</body>
</html>
```